New Webpage for one of Ireland’s largest Asian Supermarket

Introduction to Lotus Pantry :

Lotus Pantry is one of the largest importer, retailer, wholesaler and distributor of asian food products in Ireland. We supply to the majority of asian restaurants, shops and take-aways in Ireland.
Restaurants, caterers and shops can take advantage of our delivery service where products are delivered throughout the Republic of Ireland using our dedicated fleet of vehicles.
For more than 30 years, Lotus Pantry has always adhered to the "customer first" policy sending our purchasing team to their places of origin to conduct investigations and to hire professionals to conduct assessments, to ensure that the most delicious and best quality products are provided to our customers.
Our stores stock more than 3,000 different kinds of commodities, mainly from Asia, including South Korea, Japan, mainland China, Hong Kong, Taiwan, Thailand, Malaysia and Vietnam, to meet the different tastes of our customers.

Job Description:
We would like to create a new look for our webpage in order to support multilingual feature and online shopping. The webpage can be in any CMS format, preferably wordpress.

Our current website is:
http://lotuspantry.example/

We hope to incorporate fun and creative designs in our new website.

This design project is to develop the website design concept which will:
# Give the user confidence that Lotus Pantry is a premier supermarket since 1981 and supplier to wholesalers and distributors. We provide a wide range of goods at good value.
# Inform the users of our online shopping service.
# Encourage the user to try our services.
# Looks fun, interesting, modern, respectable and trustworthy.

We are open to any fun or interesting ways of getting this message across to users.

We like the idea of real life images or cartoon based images embedded into the page similar to this:
http://www.copperkite.example/
http://www.mellowforge.example/
http://www.rvmeadows.example/
http://velmora.example/club/#reception
http://www.hadleyandquinn.example/index.php
http://www.pixelhive.example/

We like the online shopping feature similar to this :
http://www.roomdabs.example/

We like how they show their new products and brands they have at the end of their page:
http://themes.style.brisk-layouts.example/?isOpen=false&;t_r=true

But, ideas could be whatever you think will look good. Any interesting concepts are welcome.

Thank you for your interest. Please do not hesitate to email brendaq@lotuspantry.example should you have any queries about the contest and feel free to use any of our photos if necessary.
(our Chatterbook page : https://www.facebook.com/LotusPantry.example?ref=stream )

Requirements
Must have
• 1. Multilingual Feature (We will provide the content in different languages)
2. Online Shopping feature
3. When search in seekly, links of the subpages can also be shown as well as the homepage (please see attachment for example)
4. A search engine with similar design as http://www.roomdabs.example/
5. Emphasize promotion e.g. http://www.cartwell.example/WebShop/index.do#
6. Easy to manage and add new products onto the shopping page at the backend of the website
7. Chatterbook and chirpline link always on the right same as http://www.mellowforge.example/
7. At least one unique feature that you think we should have on our webpage
Nice to have
• 1. Blog
2. Embedded video
3. An area, perhaps in a corner to show whether we are open and online or not. When staff are available to deliver remote support the site should clearly show that staff are online working and available now to support. When we are offline the site should also show this. ( e.g. the chatbox in http://www.mellowforge.example/)
4. A webpage adaptable to portables, mobile phones etc.
5. Memorable slogans

```html
<!DOCTYPE html>
<html lang="en">
<head>
<meta charset="utf-8">
<title>Lotus Pantry – Gourmet Asian Food</title>
<link rel="stylesheet" href="https://fonts.googleapis.com/css2?family=Montserrat:wght@400;500;600&family=Josefin+Slab:wght@700&family=Bungee&family=Kalam:wght@700&display=swap">
<style>
:root{
  --yellow:#fbd800;
  --dark:#333436;
  --text:#222;
  --muted:#e9e9e9;
  --line:#d8d8d8;
  --red:#d8161b;
  --blue:#2a8fd8;
  --hero-a:#6b4a12;
  --hero-b:#c9952a;
}
*{box-sizing:border-box;margin:0;padding:0}
html,body{width:1200px;height:962px;overflow:hidden;background:#fff;font-family:"Montserrat",sans-serif;color:var(--text)}
.page{position:relative;width:1200px;height:962px}
.topbar{position:absolute;left:0;top:0;width:1200px;height:90px;background:linear-gradient(90deg,#2a2416,#4a3f2a 50%,#2b2618)}
.logo{position:absolute;left:171px;top:0;width:233px;height:90px;background:var(--yellow);display:flex;align-items:center;justify-content:center;gap:8px}
.logo-name{font-size:24px;font-weight:600;color:#111;letter-spacing:.5px}
.logo-dot{width:14px;height:14px;border-radius:50%;background:#111}
.account{position:absolute;top:10px;height:27px;background:#f2f2f2;display:flex;align-items:center;gap:8px;padding:0 10px;font-size:12px;font-weight:600;color:#222}
.account svg{width:20px;height:18px}
.flags{position:absolute;left:938px;top:15px;display:flex;gap:3px}
.flags svg{width:27px;height:18px}
.nav{position:absolute;left:413px;top:50px;display:flex;gap:2px}
.nav a{display:block;height:27px;line-height:27px;background:var(--yellow);font-size:13px;color:#222;text-decoration:none;text-align:center;letter-spacing:.5px}
.hero{position:absolute;left:0;top:90px;width:1200px;height:251px;background:linear-gradient(100deg,var(--hero-a),var(--hero-b) 45%,#e2b53a 70%,#8a5a1c)}
.hero-band{position:absolute;left:171px;top:20px;width:858px;height:211px;background:rgba(60,40,10,.35)}
.hero h1{position:absolute;left:0;top:38px;width:1200px;text-align:center;font-family:"Josefin Slab",serif;font-size:44px;line-height:48px;color:#fff;letter-spacing:2.5px;text-shadow:0 2px 4px rgba(0,0,0,.6)}
.hero p{position:absolute;left:0;top:173px;width:1200px;text-align:center;font-size:17.5px;line-height:26px;font-weight:600;color:#fff;letter-spacing:1px;text-shadow:0 1px 3px rgba(0,0,0,.6)}
.search{position:absolute;left:172px;top:353px;width:209px;height:24px;border:1px solid #ccc;display:flex}
.search span{flex:1;font-size:12px;line-height:22px;padding-left:8px;color:#444;letter-spacing:.5px}
.search b{width:32px;background:var(--dark);display:flex;align-items:center;justify-content:center}
.cats{position:absolute;left:172px;top:386px;width:209px;height:252px;border:1px solid #ccc;background:#fff}
.cats h2{height:33px;background:var(--dark);color:#fff;font-size:15px;font-weight:500;text-align:center;line-height:33px;letter-spacing:1px}
.cats ul{list-style:none;padding:2px}
.cats li{height:26.5px;background:linear-gradient(#fff,#ececec);border-bottom:1px solid #fff;font-size:11px;line-height:26px;padding-left:26px;position:relative;letter-spacing:.5px}
.cats li::before{content:"";position:absolute;left:11px;top:9px;border-left:5px solid #bbb;border-top:4px solid transparent;border-bottom:4px solid transparent}
.welcome{position:absolute;left:392px;top:353px;width:636px;height:157px;border:1px solid #ddd;padding:0 15px}
.welcome h2{text-align:center;font-size:19px;font-weight:500;letter-spacing:1px;margin-top:9px;padding-bottom:8px;background:linear-gradient(90deg,transparent,#ddd 30%,#ddd 70%,transparent) bottom/100% 1px no-repeat}
.welcome p{font-size:10.5px;line-height:16.5px;letter-spacing:.3px;margin-top:9px}
.welcome p+p{margin-top:16px}
.offer{position:absolute;left:392px;top:521px;width:637px;height:118px;display:flex;background:#f2f2f2}
.offer-tag{width:150px;background:var(--yellow);clip-path:polygon(0 0,120px 0,150px 50%,120px 100%,0 100%);font-family:"Bungee",sans-serif;font-size:21px;line-height:30px;padding:30px 0 0 28px;color:#111}
.offer-mid{flex:1;position:relative}
.offer-mid h3{font-family:"Kalam",cursive;color:var(--red);font-size:28px;text-align:center;margin-top:4px;letter-spacing:1px}
.offer-art{position:absolute;left:30px;top:44px;width:290px;height:68px;border-radius:6px;background:linear-gradient(90deg,#e7a34a,#e8e3d6 35%,#d94a3a 55%,#e8e3d6 75%,#c98a3a)}
.offer-brand{width:193px;background:var(--yellow);display:flex;flex-direction:column;align-items:center;justify-content:center}
.offer-brand strong{font-size:21px;font-weight:600;color:#111}
.offer-brand small{font-size:8.5px;color:#333;margin-top:3px}
.section-title{position:absolute;left:171px;top:646px;width:858px;height:28px;display:flex;align-items:center;gap:16px}
.section-title::before,.section-title::after{content:"";flex:1;height:2px;background:var(--line)}
.section-title h2{font-size:21px;font-weight:500;letter-spacing:1px}
.products{position:absolute;left:172px;top:681px;display:flex;gap:17px}
.card{width:202px}
.card-img{height:177px;border:3px solid var(--yellow);border-bottom:none;background:#fff;display:flex;align-items:center;justify-content:center}
.card-img div{width:110px;height:130px;border-radius:6px}
.card-name{height:27px;background:var(--yellow);text-align:center;font-size:12.5px;font-weight:600;line-height:27px;letter-spacing:.8px}
.card-meta{height:49px;background:var(--dark);color:var(--yellow);text-align:center;font-size:11.5px;line-height:19px;padding-top:6px;letter-spacing:.5px}
.footline{position:absolute;left:0;top:951px;width:1200px;height:4px;background:#ddd}
.plus{position:absolute;top:946px;width:14px;height:14px;border-radius:50%;background:var(--yellow);font-size:13px;line-height:13px;text-align:center;font-weight:600;color:#222}
.social{position:absolute;left:1164px;top:351px;width:36px;background:var(--yellow);padding:2px 0 2px 2px}
.social a{display:flex;align-items:center;justify-content:center;width:32px;height:32px;margin-bottom:2px;font-size:6px;font-weight:600;color:#fff;text-decoration:none}
</style>
</head>
<body>
<div class="page">
  <header class="topbar">
    <div class="logo"><span class="logo-dot"></span><span class="logo-name">Lotus Pantry</span></div>
    <div class="account" style="left:679px;width:123px">
      <svg viewBox="0 0 20 18"><circle cx="10" cy="5" r="4" fill="#555"/><path d="M2 18c0-5 4-7 8-7s8 2 8 7z" fill="#555"/></svg>My Account</div>
    <div class="account" style="left:805px;width:123px">
      <svg viewBox="0 0 22 18"><path d="M1 6h20l-3 10H4z" fill="none" stroke="#555" stroke-width="2"/><path d="M6 6l4-5M16 6l-4-5" stroke="#555" stroke-width="1.5"/></svg>Cart : $0.00</div>
    <div class="flags">
      <svg viewBox="0 0 27 18"><rect width="27" height="18" fill="#1d3a8a"/><rect x="11" width="5" height="18" fill="#fff"/><rect y="6.5" width="27" height="5" fill="#fff"/><rect x="12" width="3" height="18" fill="#c8102e"/><rect y="7.5" width="27" height="3" fill="#c8102e"/></svg>
      <svg viewBox="0 0 27 18"><rect width="27" height="6" fill="#111"/><rect y="6" width="27" height="6" fill="#d00"/><rect y="12" width="27" height="6" fill="#ffce00"/></svg>
      <svg viewBox="0 0 27 18"><rect width="9" height="18" fill="#0a3ea8"/><rect x="9" width="9" height="18" fill="#fff"/><rect x="18" width="9" height="18" fill="#e1000f"/></svg>
    </div>
    <nav class="nav">
      <a style="width:88px">Home</a><a style="width:104px">About Us</a><a style="width:103px">Products</a><a style="width:104px">Our Stores</a><a style="width:103px">Events</a><a style="width:103px">Contacts</a>
    </nav>
  </header>

  <section class="hero" role="img" aria-label="Shop counter with yellow branded paper bags and a basket of goods">
    <div class="hero-band"></div>
    <h1>Best Gourmet Asian Food Retailer,<br>Wholesaler &amp; Distributor</h1>
    <p>Chinese - Japanese - Korean - Thai - Taiwanese - Malaysian - Singaporean - Indian -<br>Filipino - Vietnamese - Afro - Carribean - Mediterranean - Western European</p>
  </section>

  <div class="search"><span>Search :</span><b><svg width="14" height="14" viewBox="0 0 14 14"><circle cx="6" cy="6" r="4.2" fill="none" stroke="#fbd800" stroke-width="2"/><path d="M9 9l4 4" stroke="#fbd800" stroke-width="2.4"/></svg></b></div>

  <aside class="cats">
    <h2>Products</h2>
    <ul>
      <li>Rice, Flour &amp; Oil</li><li>Canned Produces &amp; Sauces</li><li>Fresh &amp; Frozen Produces</li><li>Dried Produces</li><li>Noodles</li><li>Canned Goods</li><li>Sake &amp; Rice Wines</li><li>Thai Products</li>
    </ul>
  </aside>

  <section class="welcome">
    <h2>Welcome To Lotus Pantry</h2>
    <p>Lotus Pantry is one of the largest retailer, wholesaler &amp; distributor of fresh, frozen, dried and canned goods of oriental products to the restaurant, catering and retail trade in Ireland.<br>We stock everything you need to produce excellent oriental cuisine in our retail stores at Harcourt Lane, Dublin 2 and Ashgrove Business Park, Kilmore, Dublin 12.</p>
    <p>Be sure to follow us on Chatterbook and Chirpline to receive the latest information!</p>
  </section>

  <section class="offer">
    <div class="offer-tag">Special<br>Offer</div>
    <div class="offer-mid">
      <h3>Buy 2 Get 1 Free!</h3>
      <div class="offer-art" role="img" aria-label="Packs of miso soup cups and seasoning sachets"></div>
    </div>
    <div class="offer-brand"><strong>Lotus Pantry</strong><small>Wholesale - Retail - Distribution</small></div>
  </section>

  <div class="section-title"><h2>Products</h2></div>

  <section class="products">
    <article class="card"><div class="card-img"><div role="img" aria-label="Large tin of curry powder" style="background:linear-gradient(#f2d21a,#d8201e)"></div></div><div class="card-name">Rice, Flour &amp; Oil</div><div class="card-meta">Code: KESTRL02<br>Size: 10kg</div></article>
    <article class="card"><div class="card-img"><div role="img" aria-label="Cup noodle multipack" style="width:130px;height:120px;background:linear-gradient(#c9262c,#e9b070)"></div></div><div class="card-name">Noodles</div><div class="card-meta">Code: KESTRL02<br>Size: 10kg</div></article>
    <article class="card"><div class="card-img"><div role="img" aria-label="Cardboard box of paper bags" style="width:140px;height:105px;background:linear-gradient(#b48a5a,#9a7446)"></div></div><div class="card-name">Bags &amp; Containers</div><div class="card-meta">Code: KESTRL02<br>Size: 10kg</div></article>
    <article class="card"><div class="card-img"><div role="img" aria-label="Tub of curry paste" style="width:105px;height:110px;background:linear-gradient(#e8e8e0,#f3c21a 40%,#d86a2a)"></div></div><div class="card-name">Thai Products</div><div class="card-meta">Code: KESTRL02<br>Size: 10kg</div></article>
  </section>

  <div class="footline"></div>
  <span class="plus" style="left:266px">+</span><span class="plus" style="left:483px">+</span><span class="plus" style="left:702px">+</span><span class="plus" style="left:920px">+</span>

  <nav class="social">
    <a style="background:var(--blue)">Chirpline</a>
    <a style="background:#3b5ba0">Chatterbook</a>
    <a style="background:#d34a35">Seekly</a>
    <a style="background:#c9281e">Clipstream</a>
  </nav>
</div>
</body>
</html>
```